Kelvor Plant Services

We are a heavy diesel mechanical business with additional air con certificates, remapping engine rebuilt

Contact Information for Business Card

Company Name, Director Name, Managing Director, Contact details, email and website

Font styles to use
Serif
Script

```html
<!DOCTYPE html>
<html lang="en">
<head>
<meta charset="utf-8">
<title>Kelvor Plant Services – Business Card</title>
<link href="https://fonts.googleapis.com/css2?family=Marcellus&display=swap" rel="stylesheet">
<style>
  :root {
    --backdrop: #5c5d5f;
    --card: #ffffff;
    --card-shade: #ececec;
    --navy: #2b2a78;
    --ink: #111111;
    --grey-text: #6b6b6b;
    --rule: #9a9a9a;
  }
  * { margin: 0; padding: 0; box-sizing: border-box; }
  html, body { width: 1200px; height: 900px; overflow: hidden; }
  body {
    background: var(--backdrop);
    font-family: "Marcellus", Georgia, serif;
    position: relative;
  }
  .card {
    position: absolute;
    width: 640px;
    height: 366px;
    background: linear-gradient(160deg, var(--card) 40%, var(--card-shade) 100%);
    box-shadow: 0 12px 28px rgba(0,0,0,0.35);
  }
  .card-front { left: 150px; top: 60px; }
  .card-back { left: 410px; top: 474px; }

  .brand {
    position: absolute;
    display: flex;
    align-items: center;
    gap: 14px;
    color: var(--navy);
    white-space: nowrap;
  }
  .brand-dot {
    border-radius: 50%;
    border: 3px solid var(--ink);
    flex: none;
  }
  .card-front .brand {
    left: 50%; top: 50%;
    transform: translate(-50%, -50%);
    font-size: 38px;
  }
  .card-front .brand-dot { width: 46px; height: 46px; }
  .card-back .brand {
    right: 40px; top: 52px;
    font-size: 26px;
  }
  .card-back .brand-dot { width: 32px; height: 32px; }

  .rule {
    position: absolute;
    left: 40px;
    right: 40px;
    height: 1px;
    background: var(--rule);
  }
  .rule-top { top: 168px; }
  .rule-bottom { top: 318px; }

  .contact {
    position: absolute;
    left: 40px;
    top: 182px;
  }
  .person-name {
    color: var(--navy);
    font-size: 22px;
    letter-spacing: 0.5px;
    text-transform: uppercase;
  }
  .person-role {
    color: var(--grey-text);
    font-size: 15px;
    margin: 2px 0 10px 12px;
  }
  .contact-list { list-style: none; }
  .contact-list li {
    display: flex;
    align-items: center;
    gap: 8px;
    color: var(--grey-text);
    font-size: 15px;
    line-height: 25px;
  }
  .contact-list svg { width: 15px; height: 15px; fill: var(--navy); flex: none; }
  .address {
    position: absolute;
    left: 40px;
    top: 328px;
    color: var(--grey-text);
    font-size: 15px;
  }
</style>
</head>
<body>
  <section class="card card-front">
    <div class="brand"><span class="brand-dot"></span>Kelvor Plant Services</div>
  </section>

  <section class="card card-back">
    <div class="brand"><span class="brand-dot"></span>Kelvor Plant Services</div>
    <div class="rule rule-top"></div>
    <div class="contact">
      <p class="person-name">Dorian Vale</p>
      <p class="person-role">Managing Director</p>
      <ul class="contact-list">
        <li>
          <svg viewBox="0 0 24 24" aria-hidden="true"><path d="M6.6 10.8a15.1 15.1 0 0 0 6.6 6.6l2.2-2.2a1 1 0 0 1 1-.25 11.4 11.4 0 0 0 3.6.57 1 1 0 0 1 1 1V20a1 1 0 0 1-1 1A17 17 0 0 1 3 4a1 1 0 0 1 1-1h3.5a1 1 0 0 1 1 1c0 1.25.2 2.45.57 3.57a1 1 0 0 1-.25 1z"/></svg>
          0491 572 306
        </li>
        <li>
          <svg viewBox="0 0 24 24" aria-hidden="true"><path d="M2 5h20v14H2z M3.5 6.5 12 13l8.5-6.5" fill="none" stroke="#2b2a78" stroke-width="2"/></svg>
          admin@kelvorplant.net
        </li>
        <li>
          <svg viewBox="0 0 24 24" aria-hidden="true"><g fill="none" stroke="#2b2a78" stroke-width="1.6"><circle cx="12" cy="12" r="9"/><ellipse cx="12" cy="12" rx="4" ry="9"/><path d="M3 12h18M5 7h14M5 17h14"/></g></svg>
          www.kelvorplant.net
        </li>
      </ul>
    </div>
    <div class="rule rule-bottom"></div>
    <p class="address">48 Larkfield Road, Millbrook, WA 6090, Australia</p>
  </section>
</body>
</html>
```